[Fun Project] Design A Website For A Semi Pro Soccer Team!

DESIGN ONLY! [NO CODING NEEDED]

Hey,

Thanks for looking! Are you ready to design a cool project with us?

This may be a once in a lifetime opportunity to design a website for a Semi Pro Soccer Team. Projects like this don't come along very often! This will be a lot of fun for you!

We need a fresh and exciting website design for a new soccer (or football, depending on where you are) team. You can view the existing site here: http://www.pwxdunefc.com/

You can get a sense of the team colors and whatnot from that, but the layout is a little dull. We need something more like this: http://www.mendelhollow.com.

We need something that is visual and exciting, something that will appeal to a sports fan. Ideally, we'd love to work with a designer is a fan of the game, as we think he/she would design something more appealing to the demographic.

Be sure to follow the link below and check out our video:

http://clipnest.com/user4417032/review/30582714/4c1d7a90fe

Thank you and good luck!

Target Market(s)

Soccer/football fans and those interested in becoming fans. More than likely, we're talking males 18-40, but don't want to rule out females.

Font styles to use
Sans Serif

Colors
faee3e
fbed22
eb1f27
000000
f6f6f6

Requirements
Must have
• Picture/video slider in the top left (see video)
1 home page design and 2 interior page designs
Should not have
• Cluttered
Dull
Lame
Poor Design
And for the love of all the is holy please do not submit us a theme or a template from some website. We are smarter then that and will just remove you from the project....REAL Designers, we got your back and won't even consider crappy stuff....

```html
<!DOCTYPE html>
<html lang="en">
<head>
<meta charset="utf-8">
<title>Pinewax Dune FC</title>
<link href="https://fonts.googleapis.com/css2?family=Roboto:wght@400;500;700&family=Michroma&display=swap" rel="stylesheet">
<style>
:root{
  --red:#eb1f27;
  --red-dark:#c8161d;
  --black:#000;
  --ink:#333;
  --muted:#888;
  --light:#f6f6f6;
  --topbar:#efefef;
  --side:#e4e4e4;
  --line:#d6d6d6;
  --white:#fff;
}
*{box-sizing:border-box;margin:0;padding:0}
html,body{width:1200px;height:1000px;overflow:hidden}
body{background:var(--black);font-family:'Roboto',sans-serif;color:var(--ink);position:relative}
.topbar{position:absolute;left:0;top:0;width:1200px;height:32px;background:var(--topbar)}
.phone{position:absolute;left:178px;top:9px;font-size:11px;color:#333;display:flex;align-items:center;gap:5px}
.follow{position:absolute;right:176px;top:9px;font-size:10px;color:#777;display:flex;align-items:center;gap:4px}
.follow .sq{width:14px;height:14px;display:inline-block}
.sq.blue{background:#3b5998}.sq.sky{background:#1da1f2}.sq.pink{background:#cb2027}.sq.red{background:#e52d27}
.side-photo{position:absolute;top:200px;width:200px;height:460px}
.side-photo.left{left:0;background:radial-gradient(ellipse at 40% 40%,#3a6a8a 0%,#1d3345 45%,#000 80%)}
.side-photo.right{right:0;background:radial-gradient(ellipse at 70% 45%,#4d7a8c 0%,#23404c 45%,#000 80%)}
.masthead{position:absolute;left:177px;top:32px;width:847px;height:132px}
.masthead .lights{position:absolute;left:120px;top:0;width:700px;height:132px;background:radial-gradient(ellipse at 20% 15%,rgba(255,255,255,.35),transparent 25%),radial-gradient(ellipse at 65% 12%,rgba(255,255,255,.35),transparent 25%),linear-gradient(#000,#1b1b1b)}
.masthead .player{position:absolute;left:540px;top:2px;width:180px;height:130px;background:radial-gradient(ellipse at center,#b08a3a 0%,#4a3a1a 45%,transparent 72%)}
.brand{position:absolute;left:112px;top:28px;display:flex;align-items:center;gap:8px}
.brand .dot{width:70px;height:70px;border-radius:50%;background:var(--red)}
.brand .name{font-family:'Roboto',sans-serif;font-weight:700;font-size:13px;color:var(--white)}
.site-title{position:absolute;left:192px;top:80px;font-family:'Michroma',sans-serif;line-height:1}
.site-title .over{color:var(--red);font-size:12.5px;letter-spacing:1px}
.site-title .main{color:#c9c9c9;font-size:25px;letter-spacing:2px;margin-top:4px}
.nav{position:absolute;left:177px;top:164px;width:847px;height:36px;background:linear-gradient(#f2353b,var(--red-dark));display:flex}
.nav a{color:var(--white);text-decoration:none;font-size:11px;font-weight:500;padding:0 15px;line-height:36px;border-right:1px solid rgba(0,0,0,.15);box-shadow:1px 0 0 rgba(255,255,255,.15)}
.search{position:absolute;right:8px;top:8px;width:198px;height:20px;background:var(--white);font-size:9.5px;font-style:italic;color:#666;padding:4px 6px}
.search svg{position:absolute;right:6px;top:5px}
.page{position:absolute;left:177px;top:200px;width:847px;height:732px;background:var(--white)}
.sidebar-bg{position:absolute;left:569px;top:0;width:278px;height:732px;background:var(--side)}
.slider{position:absolute;left:7px;top:8px;width:550px;height:278px;background:linear-gradient(135deg,#6a5a63 0%,#3a3340 40%,#b38a85 70%,#7a6a70 100%)}
.slider .dots{position:absolute;right:14px;top:10px;display:flex;gap:4px}
.slider .dots i{width:7px;height:7px;border-radius:50%;background:#ddd;display:block}
.slider .dots i.on{background:#fff;box-shadow:0 0 0 1px #999 inset}
.caption{position:absolute;left:0;bottom:0;width:100%;height:66px;background:rgba(0,0,0,.6);padding:12px 14px;color:var(--white)}
.caption h2{font-size:18px;font-weight:500}
.caption p{font-size:12px;margin-top:7px}
.schedule{position:absolute;left:7px;top:293px;width:550px;height:34px;background:linear-gradient(#f2353b,var(--red-dark));color:var(--white);font-size:12px;font-weight:700;text-align:center;line-height:34px}
.cards{position:absolute;left:7px;top:335px;display:flex;gap:8px}
.card{width:178px;height:237px;border:1px solid var(--line);background:var(--white)}
.card .thumb{height:104px}
.card .body{padding:10px 9px}
.card h3{color:var(--red);font-size:11.5px;font-weight:700;line-height:14px}
.card time{display:block;font-size:8px;color:var(--muted);margin-top:6px}
.card p{font-size:9px;line-height:13.5px;margin-top:5px;color:#444}
.card .more{font-size:9px;color:var(--red);margin-top:8px;display:block}
.scrollbar{position:absolute;left:7px;top:587px;width:550px;height:16px;background:#eee;border:1px solid #ddd}
.scrollbar .thumb-bar{position:absolute;left:17px;top:3px;width:126px;height:9px;border-radius:5px;background:#c5c5c5}
.intro{position:absolute;left:8px;top:617px;width:548px;font-size:9.2px;line-height:13.3px;color:#444}
.widget{position:absolute;left:580px;width:260px;background:var(--white)}
.widget .head{height:33px;background:var(--red);color:var(--white);font-size:13.5px;font-weight:500;padding:9px 7px}
.radio{top:8px;height:117px}
.radio .badge{position:absolute;left:10px;top:44px;width:90px;height:62px;background:#f5d000;display:flex;align-items:center;justify-content:center;font-weight:700;font-size:13px;color:var(--red)}
.radio p{position:absolute;left:117px;top:60px;font-size:9.5px;line-height:13.5px;color:#555}
.standings{top:133px;height:85px}
.standings table{width:246px;margin:10px 7px;font-size:9px;border-collapse:collapse;color:#444}
.standings td{padding:3px 0;text-align:center}
.standings td:first-child{text-align:left;width:90px}
.social{position:absolute;left:580px;top:226px;width:260px;height:223px;background:var(--white);border:1px solid #bcc4d6;padding:7px}
.social .top{display:flex;gap:6px}
.social .icon{width:36px;height:36px;background:#3b5998}
.social .name{font-size:10.5px;font-weight:500;color:#3b5998}
.social .like{margin-top:3px;display:inline-block;font-size:8.5px;background:#4c66a4;color:#fff;padding:2px 5px}
.social .count{font-size:8px;margin-top:9px;color:#333}
.social .grid{display:grid;grid-template-columns:repeat(6,36px);gap:4px;margin-top:7px}
.social .grid span{height:36px;background:#8a7f78}
.social .foot{border-top:1px solid #ddd;margin-top:8px;padding-top:4px;font-size:7px;color:#777}
.footer{position:absolute;left:0;width:1200px;text-align:center;color:#999;font-size:9.5px}
</style>
</head>
<body>
<div class="topbar">
  <div class="phone"><svg width="10" height="10" viewBox="0 0 24 24"><path d="M6.6 10.8a15 15 0 006.6 6.6l2.2-2.2c.3-.3.7-.4 1-.2 1.1.4 2.3.6 3.6.6.6 0 1 .4 1 1V20c0 .6-.4 1-1 1A17 17 0 013 4c0-.6.4-1 1-1h3.5c.6 0 1 .4 1 1 0 1.3.2 2.5.6 3.6.1.3 0 .7-.2 1z" fill="#333"/></svg>Call Us: (555) 010-4821</div>
  <div class="follow">Follow Us: <span class="sq blue"></span><span class="sq sky"></span><span class="sq pink"></span><span class="sq red"></span></div>
</div>

<div class="side-photo left" role="img" aria-label="Soccer player in light blue kit on a stadium pitch"></div>
<div class="side-photo right" role="img" aria-label="Goalkeeper celebrating on his knees on the grass"></div>

<header class="masthead">
  <div class="lights" role="img" aria-label="Stadium floodlights at night"></div>
  <div class="player" role="img" aria-label="Player in yellow kit performing an overhead kick"></div>
  <div class="brand"><span class="dot"></span><span class="name">Pinewax Dune FC</span></div>
  <div class="site-title"><div class="over">OFFICIAL SITE OF THE</div><div class="main">PINEWAX DUNE</div></div>
</header>

<nav class="nav">
  <a>HOME</a><a>NEWS</a><a>STATE</a><a>ABOUT</a><a>CONTACT</a><a>TEAM SHOP</a><a>THE NDL</a>
  <div class="search">Type to search
    <svg width="10" height="10" viewBox="0 0 10 10"><circle cx="4" cy="4" r="3" stroke="#000" stroke-width="1.5" fill="none"/><line x1="6.2" y1="6.2" x2="9.3" y2="9.3" stroke="#000" stroke-width="1.6"/></svg>
  </div>
</nav>

<main class="page">
  <div class="sidebar-bg"></div>
  <section class="slider" role="img" aria-label="Two players contesting the ball during a match">
    <div class="dots"><i class="on"></i><i></i><i class="on"></i><i class="on"></i></div>
    <div class="caption"><h2>Watch: Kessler 'on the road'</h2><p>Midfielder shoots behind-the-scenes video leading up to Ridgeport match</p></div>
  </section>
  <div class="schedule">DOWNLOAD AND PRINT THE 2014 PINEWAX DUNE FULL SCHEDULE!</div>

  <div class="cards">
    <article class="card"><div class="thumb" role="img" aria-label="Players challenging for the ball in a stadium" style="background:linear-gradient(#9aa2a8,#6b5a4a)"></div>
      <div class="body"><h3>OFFICIAL PRESS RELEASE FROM THE NDL ON PWX...</h3><time>December 5, 2013</time><p>BAYFORD – The NDL is pleased to welcome the Pinewax Dune FC to the league for the 2014 season.</p><span class="more">Read More ›</span></div></article>
    <article class="card"><div class="thumb" role="img" aria-label="Goalkeeper diving for a save" style="background:linear-gradient(#b7b9b4,#6f8a4a)"></div>
      <div class="body"><h3>OFFICIAL PRESS RELEASE FROM THE NDL ON PWX...</h3><time>December 5, 2013</time><p>BAYFORD – The NDL is pleased to welcome the Pinewax Dune FC to the league for the 2014 season.</p><span class="more">Read More ›</span></div></article>
    <article class="card"><div class="thumb" role="img" aria-label="Player in red kit chasing the ball" style="background:linear-gradient(#a9b3a6,#b0483e)"></div>
      <div class="body"><h3>OFFICIAL PRESS RELEASE FROM THE NDL ON PWX...</h3><time>December 5, 2013</time><p>BAYFORD – The NDL is pleased to welcome the Pinewax Dune FC to the league for the 2014 season.</p><span class="more">Read More ›</span></div></article>
  </div>

  <div class="scrollbar">
    <svg style="position:absolute;left:4px;top:3px" width="6" height="8"><path d="M5 0L0 4l5 4z" fill="#999"/></svg>
    <div class="thumb-bar"></div>
    <svg style="position:absolute;right:4px;top:3px" width="6" height="8"><path d="M0 0l6 4-6 4z" fill="#999"/></svg>
  </div>

  <p class="intro">NDL Soccer is coming to Pinewax! The NDL is the top developmental men's league in North America. The 2013 NDL featured 64 teams within four conferences throughout the United States and Canada. The NDL season consists of 14 regular season matches for each team, seven home and seven away, and provides elite collegiate players the opportunity to taste a higher level of competition while maintaining their eligibility. In addition to league play, NDL teams compete in the Harmon Open Cup as well as various exhibitions. The NDL has proven to be an important stepping-stone for top professionals now playing throughout the world.</p>

  <aside class="widget radio">
    <div class="head">CHECK US OUT ON THE RADIO!</div>
    <div class="badge">KDNE 98.3</div>
    <p>Team President Dale Morrow sits<br>down with 98.3 KDNE Radio!</p>
  </aside>

  <aside class="widget standings">
    <div class="head">STANDINGS</div>
    <table>
      <tr><td>Pos</td><td>P</td><td>W</td><td>D</td><td>L</td><td>F</td><td>A</td><td>GD</td><td>Pts</td></tr>
      <tr><td>Pinewax Dune</td><td>0</td><td>0</td><td>0</td><td>0</td><td>0</td><td>0</td><td>0</td><td>0</td></tr>
    </table>
  </aside>

  <aside class="social">
    <div class="top"><div class="icon"></div><div><div class="name">Campfire Builders</div><span class="like">Like</span></div></div>
    <div class="count">2,987,595 people like <span style="color:#3b5998">Campfire Builders</span>.</div>
    <div class="grid" role="img" aria-label="Grid of follower profile photos">
      <span></span><span></span><span></span><span></span><span></span><span></span>
      <span></span><span></span><span></span><span></span><span></span><span></span>
      <span></span><span></span><span></span><span></span><span></span><span></span>
    </div>
    <div class="foot">Campfire social plugin</div>
  </aside>
</main>

<div class="footer" style="top:952px">© 2013 Pinewax Dune. All rights reserved.</div>
<div class="footer" style="top:973px">Powered by Pinewax internet marketing company Granite Web Studio.</div>
</body>
</html>
```